Task and Project Management Tool Website

We need designs for both desktop and mobile for a new site, which is the marketing presentation of our new platform called Tilebeam, which is a task and project tool specific for the property sector. The name refers to people working on different workstreams on a property and crossing their paths when collaborating. The site will not do ecommerce, just a presentation of the product. We would like to include a video (no voice over) and some graphics, which we will do separately. The whole site will include a few pages, as detailed in the attach document. The product appeals to property companies and banks, hence the brand should portray reliability, corporate. We would like to see combinations of black, white and blue.
Updates

This project is currently put on hold. Client will be focusing on getting a Logo design first. Then once the logo has been created, we will resume this project and use the logo on the web designs submissions. Regards, DC Admin Osgood

Logo design has been completed. Please resubmit and submit new web designs on this project using the logo design attached. Regards, DC Admin Osgood

Target Market(s)

Corporate (B2B)

Logo Text

Tilebeam

Coding

Coded - Design and coding required

Number of Pages Required

5+ page

Requirements
Must have
• As in the specs
Should not have
• pictures of fake people (we prefer icons)

```html
<!DOCTYPE html>
<html lang="en">
<head>
<meta charset="utf-8">
<title>Tilebeam – Schedule a Demo</title>
<link rel="stylesheet" href="https://fonts.googleapis.com/css2?family=Open+Sans:wght@400;600;700&display=swap">
<style>
:root{
  --brand:#0a8cf0;
  --ink:#333a44;
  --line:#d6d9de;
  --footer:#00399e;
  --footer-deep:#012f86;
  --footer-shade:#0a3690;
  --white:#ffffff;
}
*{box-sizing:border-box;margin:0;padding:0}
html,body{width:1200px;height:887px;overflow:hidden;background:var(--white)}
body{font-family:"Open Sans",Arial,sans-serif;color:var(--ink);position:relative}
.site-header{position:absolute;left:0;top:0;width:1200px;height:78px;background:var(--white);
  box-shadow:0 8px 14px -10px rgba(0,0,0,.12)}
.brand{position:absolute;left:143px;top:17px;display:flex;align-items:center;gap:10px;color:var(--brand);
  font-size:29px;font-weight:400;letter-spacing:.2px}
.brand-dot{width:14px;height:14px;border-radius:50%;background:var(--brand)}
.main-nav a{position:absolute;top:33px;font-size:15px;color:var(--ink);text-decoration:none}
.demo-title{position:absolute;left:0;width:1200px;top:140px;text-align:center;color:var(--brand);
  font-size:34px;font-weight:400}
.field{position:absolute;border:1px solid var(--line);background:var(--white);display:flex;align-items:flex-start;
  padding:0 0 0 10px;font-size:12px;color:var(--ink)}
.field svg{flex:none;margin-right:9px}
.field-user{left:253px;top:212px;width:339px;height:49px;align-items:center}
.field-pass{left:608px;top:212px;width:339px;height:49px;align-items:center}
.field-message{left:253px;top:280px;width:694px;height:99px;padding-top:14px}
.field-message span{line-height:20px}
.submit{position:absolute;left:553px;top:407px;width:94px;height:39px;background:var(--brand);color:var(--white);
  border:0;font-family:inherit;font-size:14px;font-weight:600;letter-spacing:.3px}
.site-footer{position:absolute;left:0;top:523px;width:1200px;height:364px;background:var(--footer);color:var(--white);overflow:hidden}
.skyline{position:absolute;left:0;bottom:30px;width:1200px;height:150px;
  background:linear-gradient(to bottom,rgba(0,57,158,0),var(--footer-shade) 70%)}
.footer-brand{position:absolute;left:141px;top:118px;display:flex;align-items:center;gap:14px;font-size:56px;font-weight:400}
.footer-brand .brand-dot{width:22px;height:22px;background:var(--white)}
.footer-heading{position:absolute;top:80px;font-size:19px;font-weight:400}
.links{position:absolute;list-style:none;font-size:13px}
.links li{height:28.3px;display:flex;align-items:center}
.links li::before{content:"›";width:18px;font-size:14px;margin-left:0}
.contact{position:absolute;font-size:13px;line-height:20px}
.contact svg{position:absolute;left:-31px}
.bottom-bar{position:absolute;left:0;bottom:0;width:1200px;height:54px;background:var(--footer-deep);
  border-top:1px solid rgba(255,255,255,.18);font-size:13px}
.copyright{position:absolute;left:143px;top:16px}
.follow{position:absolute;left:895px;top:16px}
.social{position:absolute;top:11px;width:26px;height:26px;border:1.5px solid var(--white);border-radius:50%}
</style>
</head>
<body>
<header class="site-header">
  <div class="brand"><span class="brand-dot"></span>Tilebeam</div>
  <nav class="main-nav">
    <a href="#" style="left:630px">Home</a>
    <a href="#" style="left:716px">Product</a>
    <a href="#" style="left:812px">Tilebid</a>
    <a href="#" style="left:914px">About</a>
    <a href="#" style="left:998px">Contacts</a>
  </nav>
</header>

<main>
  <h1 class="demo-title">Schedule a Demo</h1>
  <div class="field field-user">
    <svg width="16" height="16" viewBox="0 0 16 16" fill="none" stroke="#0a8cf0" stroke-width="1.3"><circle cx="8" cy="5" r="3.3"/><path d="M2 15c0-3.5 2.7-5.5 6-5.5s6 2 6 5.5"/></svg>
    <span>Username</span>
  </div>
  <div class="field field-pass">
    <svg width="16" height="17" viewBox="0 0 16 17" fill="none" stroke="#0a8cf0" stroke-width="1.3"><rect x="2" y="7" width="12" height="9" rx="1"/><path d="M4.5 7V4.8a3.5 3.5 0 0 1 7 0V7M8 10.5v2.5"/></svg>
    <span>Password</span>
  </div>
  <div class="field field-message">
    <svg width="19" height="19" viewBox="0 0 19 19" fill="none" stroke="#0a8cf0" stroke-width="1.3"><path d="M9 3H2v14h14v-7"/><path d="M15 1.5l2.5 2.5-8 8H7v-2.5z"/></svg>
    <span>Message</span>
  </div>
  <button class="submit" type="button">SUBMIT</button>
</main>

<footer class="site-footer">
  <div class="skyline" role="img" aria-label="Faint city skyline silhouette with observation wheel and clock tower"></div>
  <div class="footer-brand"><span class="brand-dot"></span>Tilebeam</div>

  <h2 class="footer-heading" style="left:524px">Quick Links</h2>
  <ul class="links" style="left:524px;top:117px">
    <li>Home</li><li>Product</li><li>Tilebid</li><li>About</li><li>Contacts</li>
  </ul>
  <ul class="links" style="left:644px;top:117px">
    <li>Disclaimer</li><li>Privacy Policy</li>
  </ul>

  <h2 class="footer-heading" style="left:868px">Contacts Details</h2>
  <div class="contact" style="left:898px;top:121px">
    <svg width="14" height="18" viewBox="0 0 14 18" fill="none" stroke="#fff" stroke-width="1.2"><path d="M7 17s6-6.2 6-10.5a6 6 0 0 0-12 0C1 10.8 7 17 7 17z"/><circle cx="7" cy="6.5" r="2"/></svg>
    <strong>Marrowgate (UK) Ltd.</strong><br>14-16 Harlow Quay<br>London SE9 4QN
  </div>
  <div class="contact" style="left:898px;top:201px">
    <svg width="16" height="16" viewBox="0 0 16 16" fill="none" stroke="#fff" stroke-width="1.2"><path d="M3 1.5l3 3-1.6 2a9 9 0 0 0 5 5l2-1.6 3 3-2 2C6.5 15 1 9.5 1 3.5z"/></svg>
    +1 555 014 2287
  </div>
  <div class="contact" style="left:898px;top:234px">
    <svg width="17" height="13" viewBox="0 0 17 13" fill="none" stroke="#fff" stroke-width="1.2"><rect x="1" y="1" width="15" height="11"/><path d="M1 1l7.5 6L16 1"/></svg>
    team@marrowgate.example
  </div>

  <div class="bottom-bar">
    <span class="copyright">Copyright © 2020 Tilebeam. All Rights Reserved.</span>
    <span class="follow">Follow Us</span>
    <span class="social" style="left:965px" aria-label="Social profile"></span>
    <span class="social" style="left:999px" aria-label="Social profile"></span>
    <span class="social" style="left:1033px" aria-label="Social profile"></span>
  </div>
</footer>
</body>
</html>
```